Atelier Mirou

I am actually making my own traditional french food.
Everything is homemade with passion.
I make differente terrines, jams, macaroons, rillettes and much more
I do as well cocktail party and catering

Hello everyone,

On the business card I would like to see appear if it's possible these following informations: traditional french food, cocktail party and catering.

```html
<!DOCTYPE html>
<html lang="fr">
<head>
<meta charset="utf-8">
<title>Atelier Mirou — Business Card</title>
<link rel="stylesheet" href="https://fonts.googleapis.com/css2?family=Alegreya:wght@400;700&display=swap">
<style>
  :root {
    --backdrop: #3b3b3d;
    --card-white: #fbfbfa;
    --card-red: #b91f2f;
    --ink: #1d1d1d;
    --paper-text: #ffffff;
    --shadow: rgba(0, 0, 0, 0.35);
  }
  * { margin: 0; padding: 0; box-sizing: border-box; }
  html, body {
    width: 1200px;
    height: 926px;
    overflow: hidden;
    background: var(--backdrop);
    font-family: "Alegreya", Georgia, serif;
  }
  .canvas {
    width: 1200px;
    height: 926px;
    display: flex;
    align-items: center;
    justify-content: center;
    gap: 60px;
  }
  .card {
    width: 520px;
    height: 297px;
    border-radius: 2px;
    box-shadow: 0 10px 28px var(--shadow);
    position: relative;
  }
  .card--front {
    background: var(--card-white);
    display: flex;
    flex-direction: column;
    align-items: center;
    justify-content: center;
    gap: 22px;
  }
  .brand {
    display: flex;
    align-items: center;
    gap: 14px;
  }
  .brand__dot {
    width: 22px;
    height: 22px;
    border-radius: 50%;
    background: var(--card-red);
  }
  .brand__name {
    font-size: 40px;
    font-weight: 400;
    letter-spacing: 0.06em;
    text-transform: uppercase;
    color: var(--ink);
  }
  .services {
    list-style: none;
    display: flex;
    gap: 10px;
    font-size: 15px;
    font-weight: 400;
    letter-spacing: 0.12em;
    text-transform: uppercase;
    color: var(--card-red);
  }
  .services__item + .services__item::before {
    content: "·";
    margin-right: 10px;
  }
  .card--back {
    background: var(--card-red);
    color: var(--paper-text);
    padding: 44px 0 0 62px;
  }
  .person {
    font-size: 33px;
    font-weight: 400;
    letter-spacing: 0.02em;
  }
  .person__surname { font-weight: 700; }
  .divider {
    width: 40px;
    height: 2px;
    background: var(--paper-text);
    margin: 20px 0 0 150px;
  }
  .contact {
    list-style: none;
    margin: 18px 0 0 8px;
    font-size: 19px;
    line-height: 1.45;
    letter-spacing: 0.03em;
  }
  .contact__label { font-weight: 700; }
</style>
</head>
<body>
  <main class="canvas">
    <section class="card card--front" aria-label="Card front">
      <div class="brand">
        <span class="brand__dot"></span>
        <span class="brand__name">Atelier Mirou</span>
      </div>
      <ul class="services">
        <li class="services__item">Traditional French Food</li>
        <li class="services__item">Cocktail Party</li>
        <li class="services__item">Catering</li>
      </ul>
    </section>
    <section class="card card--back" aria-label="Card back">
      <h1 class="person">Julien <span class="person__surname">Vasseur</span></h1>
      <div class="divider"></div>
      <ul class="contact">
        <li><span class="contact__label">Email:</span> bonjour@mirou.fr</li>
        <li><span class="contact__label">Phone:</span> 0412345678</li>
        <li><span class="contact__label">ABN:</span> 98765432100</li>
      </ul>
    </section>
  </main>
</body>
</html>
```